Seed Oil Safety Card for Healthy Restaurant Dining

I am seeking a design for a physical card to communicate my wife's health-related dietary restriction regarding seed oils. This card will be given to restaurant waiters to ensure her meals are prepared without seed oils, as it is a health issue and not merely a preference.
My wife cannot eat any “seed oil” or “processed oil”, including:
- Vegetable oil
- Canola oil
- Soybean oil
- Sunflower oil
- Corn oil
- Cottonseed oil
- Safflower oil
- Peanut oil
- Sesame oil
Oils that are OK for her to consume:
- Butter (most preferable)
- Extra virgin olive oil
- Avocado oil
- Coconut oil
- Ghee
- Lard
- Any other animal-based fats
Key Design Requirements:
- Clarity and speed of communication: The card should be easily read and understood by waiters, even in low-light environments, emphasizing that it's a health concern.
- Avoid common misconceptions: Ensure the design doesn't imply common dietary preferences like "vegetarian" or "no butter." Animal fats and butter are actually preferable for her!
- Preferred term: Use "seed oils" as the term to describe what she cannot eat due to her health issue.
- Trace amounts are acceptable: Communicate that it's OK to use cookware that has previously been in contact with seed oils, but not to have seed oil as an ingredient. Please suggest a concise way to convey this.
- Card dimensions: Design should be 3.5” x 2.25” (standard credit-card size on cardlora-print.test). Horizontal or vertical layouts are both fine, whichever makes the message clearer.
Design Suggestions:
- Utilize bold and easy-to-read typography to communicate the main message.
- Consider incorporating relevant icons or graphics that help convey the message without adding confusion.
- Use contrasting colors to enhance readability, especially in low-light situations.
- To communicate the “trace amounts OK” part, consider phrases such as:
- "Cross-contamination acceptable"
- “Used cookware OK, no ingredient use”
- “Separate cookware not necessary”
Thank you for your assistance in creating this essential card for my wife's health and safety when dining out!

```html
<!DOCTYPE html>
<html lang="en">
<head>
<meta charset="utf-8">
<title>Seed Oil Restriction Card</title>
<link rel="stylesheet" href="https://fonts.googleapis.com/css2?family=Bebas+Neue&family=Open+Sans:wght@700&display=swap">
<style>
  :root {
    --page-bg: #ffffff;
    --red-dark: #8f0008;
    --red: #d40000;
    --green-bright: #06b812;
    --green-dark: #005f1c;
    --band-black: #000000;
    --white: #ffffff;
    --warning-yellow: #f2b300;
    --title-red: #e0000b;
    --photo-grey: #8d8d8b;
    --photo-oil: #b8962e;
  }
  * { margin: 0; padding: 0; box-sizing: border-box; }
  html, body { width: 849px; height: 1200px; overflow: hidden; background: var(--page-bg); }
  .canvas { position: relative; width: 849px; height: 1200px; }

  .card {
    position: absolute;
    top: 487px;
    width: 350px;
    height: 225px;
    border-radius: 11px;
    overflow: hidden;
    box-shadow: 0 0 0 1px #e3e3e3;
  }
  .card--back { left: 63px; }
  .card--front { left: 437px; }

  /* Back side */
  .panel { position: absolute; top: 0; height: 193px; }
  .panel--banned {
    left: 0; width: 100%;
    background: linear-gradient(90deg, var(--red-dark), var(--red) 60%);
  }
  .panel--allowed {
    left: 0; width: 100%;
    clip-path: polygon(51.3% 0, 100% 0, 100% 100%, 46.3% 100%);
    background: linear-gradient(90deg, var(--green-bright) 45%, var(--green-dark));
  }
  .footer-band {
    position: absolute; left: 0; bottom: 0; width: 100%; height: 32px;
    background: var(--band-black);
    display: flex; align-items: center; justify-content: center; gap: 6px;
    padding-right: 4px;
  }
  .footer-band__text {
    font-family: 'Open Sans', sans-serif; font-weight: 700; font-size: 9px;
    color: var(--white); letter-spacing: 0.2px;
  }
  .status-icon { position: absolute; top: 17px; width: 24px; height: 24px; }
  .status-icon--banned { left: 30px; }
  .status-icon--allowed { left: 212px; }
  .heading { position: absolute; top: 14px; font-family: 'Bebas Neue', sans-serif; color: var(--white); line-height: 1; }
  .heading--banned { left: 66px; }
  .heading--allowed { left: 247px; }
  .heading__title {
    display: block; font-size: 17px; letter-spacing: 0.2px;
    -webkit-text-stroke: 0.6px #222; text-shadow: 1px 1px 0 #333;
  }
  .heading__sub { display: block; font-size: 11.5px; margin-top: 1px; }
  .oil-list { position: absolute; list-style: none; font-family: 'Bebas Neue', sans-serif; color: var(--white); }
  .oil-list--banned {
    left: 18px; width: 152px; top: 57px; text-align: center;
    font-size: 13.5px; line-height: 16.6px;
  }
  .oil-list--allowed {
    left: 195px; top: 59px; font-size: 15px; line-height: 18.4px; letter-spacing: 0.2px;
  }
  .oil-list__note { font-size: 9px; }

  /* Front side */
  .cover-photo {
    position: absolute; inset: 0;
    background: radial-gradient(ellipse at 55% 55%, var(--photo-oil) 0%, #a39a6e 35%, var(--photo-grey) 75%);
  }
  .prohibition-mark { position: absolute; inset: 0; width: 100%; height: 100%; }
  .title-band {
    position: absolute; left: 0; top: 89px; width: 100%; height: 46px;
    background: rgba(255,255,255,0.82);
    display: flex; align-items: center; justify-content: center;
  }
  .title-band__text {
    font-family: 'Bebas Neue', sans-serif; font-size: 46px; line-height: 1;
    color: var(--title-red); padding-top: 4px; letter-spacing: -0.3px;
  }
</style>
</head>
<body>
<div class="canvas">

  <section class="card card--back" aria-label="Card back: oil guide">
    <div class="panel panel--banned"></div>
    <div class="panel panel--allowed"></div>

    <svg class="status-icon status-icon--banned" viewBox="0 0 24 24" aria-hidden="true">
      <circle cx="12" cy="12" r="10.5" fill="none" stroke="#fff" stroke-width="2"/>
      <path d="M8 8l8 8M16 8l-8 8" stroke="#fff" stroke-width="2" stroke-linecap="round"/>
    </svg>
    <div class="heading heading--banned">
      <span class="heading__title">Processed Oil</span>
      <span class="heading__sub">Not allowed</span>
    </div>
    <ul class="oil-list oil-list--banned">
      <li>• Corn oil &nbsp;• Canola oil</li>
      <li>• Peanut oil • Sesame oil</li>
      <li>• Soybean oil</li>
      <li>• Safflower oil</li>
      <li>• Sunflower oil</li>
      <li>• Vegetable oil</li>
      <li>• Cottonseed oil</li>
    </ul>

    <svg class="status-icon status-icon--allowed" viewBox="0 0 24 24" aria-hidden="true">
      <path d="M21 8.5A10 10 0 1 1 16.5 3" fill="none" stroke="#fff" stroke-width="2" stroke-linecap="round"/>
      <path d="M7 11.5l4.5 4.5L22 4.5" fill="none" stroke="#fff" stroke-width="2.4" stroke-linecap="round" stroke-linejoin="round"/>
    </svg>
    <div class="heading heading--allowed">
      <span class="heading__title">Natural Oil</span>
      <span class="heading__sub">Allowed</span>
    </div>
    <ul class="oil-list oil-list--allowed">
      <li>• Butter <span class="oil-list__note">(most preferable)</span></li>
      <li>• Extra virgin olive oil</li>
      <li>• Animal - based fats</li>
      <li>• Avocado oil</li>
      <li>• Coconut oil</li>
      <li>• Lard • Ghee</li>
    </ul>

    <div class="footer-band">
      <svg width="14" height="12" viewBox="0 0 14 12" aria-hidden="true">
        <path d="M7 1L13 11H1Z" fill="none" stroke="var(--warning-yellow)" stroke-width="1" stroke-linejoin="round"/>
        <path d="M7 4.5v3.2" stroke="var(--warning-yellow)" stroke-width="1.1"/>
        <circle cx="7" cy="9.3" r="0.6" fill="var(--warning-yellow)"/>
      </svg>
      <span class="footer-band__text">Cross-contamination acceptable</span>
    </div>
  </section>

  <section class="card card--front" aria-label="Card front: title">
    <div class="cover-photo" role="img" aria-label="Photo of bottles of cooking oil lying on a grey surface"></div>
    <svg class="prohibition-mark" viewBox="0 0 350 225" aria-hidden="true">
      <circle cx="175" cy="112.5" r="93" fill="none" stroke="rgba(255,255,255,0.85)" stroke-width="13"/>
      <line x1="109" y1="46.5" x2="241" y2="178.5" stroke="rgba(255,255,255,0.85)" stroke-width="13"/>
    </svg>
    <div class="title-band">
      <h1 class="title-band__text">Food Restriction Card</h1>
    </div>
  </section>

</div>
</body>
</html>
```